New modern business card design

To design a brand new business card that's clean & modern in terms of layout.
I have attached our company logo and also basic information regarding what is needed on the card that also needs to be editable.

Target Market(s)

motor trade

Contact Information for Business Card

logo, name, title, tel, mob, email, address, www, all information is in the word.doc file

Requirements
Must have
• white background
Nice to have
• Nice clean font

```html
<!DOCTYPE html>
<html lang="en">
<head>
<meta charset="utf-8">
<title>Bolt Forge Ltd – Business Card</title>
<link href="https://fonts.googleapis.com/css2?family=Roboto:wght@400;500&family=Roboto+Condensed:wght@700&display=swap" rel="stylesheet">
<style>
  :root {
    --backdrop: #2b2b2b;
    --card-white: #f3f3f3;
    --brand-blue: #1e6eb4;
    --text-dark: #444444;
    --text-grey: #9a9a9a;
    --rule-grey: #c9c9c9;
    --white: #ffffff;
  }
  * { margin: 0; padding: 0; box-sizing: border-box; }
  html, body { width: 1200px; height: 960px; overflow: hidden; }
  body {
    position: relative;
    background: var(--backdrop);
    font-family: "Roboto", Arial, sans-serif;
  }
  .card {
    position: absolute;
    width: 600px;
    height: 343px;
  }
  .card--front { left: 314px; top: 113px; background: var(--card-white); }
  .card--back { left: 311px; top: 472px; background: var(--brand-blue); }

  .brand {
    position: absolute;
    display: flex;
    align-items: center;
    gap: 10px;
    font-weight: 500;
    letter-spacing: 1px;
    white-space: nowrap;
  }
  .brand__mark { width: 18px; height: 18px; flex: none; }
  .card--front .brand {
    left: 50px; top: 155px; width: 240px; justify-content: center;
    font-size: 26px; color: var(--brand-blue);
  }
  .card--front .brand__mark { background: var(--brand-blue); }
  .card--back .brand {
    left: 0; top: 178px; width: 600px; justify-content: center;
    font-size: 32px; color: var(--white);
  }
  .card--back .brand__mark { background: var(--white); width: 22px; height: 22px; }

  .divider {
    position: absolute;
    left: 321px; top: 72px;
    width: 1px; height: 200px;
    background: var(--rule-grey);
  }

  .contact { position: absolute; left: 347px; top: 75px; }
  .contact__name {
    font-family: "Roboto Condensed", Arial, sans-serif;
    font-weight: 700;
    font-size: 21px;
    color: var(--brand-blue);
    line-height: 24px;
  }
  .contact__title {
    font-size: 15px;
    color: var(--text-grey);
    line-height: 18px;
    letter-spacing: 0.3px;
  }
  .contact__address {
    margin-top: 11px;
    font-style: normal;
    font-size: 14.5px;
    line-height: 18px;
    color: var(--text-dark);
  }
  .contact__list { list-style: none; margin-top: 9px; }
  .contact__item {
    display: flex; align-items: center; gap: 8px;
    font-size: 14.5px; line-height: 19px; color: var(--text-dark);
  }
  .contact__icon { width: 14px; height: 14px; flex: none; fill: var(--brand-blue); }

  .back__url {
    position: absolute;
    left: 0; top: 288px; width: 600px;
    text-align: center;
    font-size: 15px;
    letter-spacing: 4px;
    color: var(--white);
  }
</style>
</head>
<body>
  <section class="card card--front" aria-label="Business card front">
    <div class="brand"><span class="brand__mark"></span>BOLT FORGE LTD</div>
    <div class="divider"></div>
    <div class="contact">
      <p class="contact__name">DANIEL MARSH</p>
      <p class="contact__title">GENERAL MANAGER</p>
      <address class="contact__address">
        Kingsley Road<br>
        Ashford Vale, Northbridge<br>
        NB7 2QT
      </address>
      <ul class="contact__list">
        <li class="contact__item">
          <svg class="contact__icon" viewBox="0 0 16 16" aria-hidden="true"><path d="M3.6 1.2l2.3 2.6-1.3 2a9 9 0 0 0 5.6 5.6l2-1.3 2.6 2.3-1.4 2.4C7.2 14.6 1.4 8.8 1.2 2.6z"/></svg>
          0100 555 2468
        </li>
        <li class="contact__item">
          <svg class="contact__icon" viewBox="0 0 16 16" aria-hidden="true"><path d="M4.5 0.5h7a1 1 0 0 1 1 1v13a1 1 0 0 1-1 1h-7a1 1 0 0 1-1-1v-13a1 1 0 0 1 1-1zM5 2.5v9.5h6V2.5zM8 12.7a0.9 0.9 0 1 0 0 1.8a0.9 0.9 0 1 0 0-1.8z"/></svg>
          07700 900 418
        </li>
        <li class="contact__item">
          <svg class="contact__icon" viewBox="0 0 16 16" aria-hidden="true"><path d="M1 3.5h14v1L8 9 1 4.5zM1 6l7 4.5L15 6v6.5H1z"/></svg>
          dmarsh@boltforge.co.uk
        </li>
        <li class="contact__item">
          <svg class="contact__icon" viewBox="0 0 16 16" aria-hidden="true"><circle cx="8" cy="8" r="7"/><path d="M4 5c1.5 0 2 1 3 1.5S6 9 5 9 3.5 7 4 5zM9 10c1-.5 2.5 0 2.5 1.5S10 13 9.5 12 8.5 10.5 9 10z" fill="#ffffff"/></svg>
          www.boltforge.co.uk
        </li>
      </ul>
    </div>
  </section>

  <section class="card card--back" aria-label="Business card back">
    <div class="brand"><span class="brand__mark"></span>BOLT FORGE LTD</div>
    <p class="back__url">www.boltforge.co.uk</p>
  </section>
</body>
</html>
```